Business card design needed for a security services business.

We provide a wide range of security services from guard personnel to electronic systems.

Industry/Entity Type

Security Industry

Contact Information for Business Card

Brent Holloway, Owner Office: 780.555.0148; Cell: 780.555.0193 Email: brent@korvanshieldgroup.example; Address 20417 163 St Edmonton, AB T5X 2K8

Colors
0054AA
0677BA
7BADD7
CADEEF
E8F1F8

Requirements
Nice to have
• On the back of the card I would like to possible list the services I provide: Guards Mobiles Live Video Surveillance Access Intrusion

```html
<!DOCTYPE html>
<html lang="en">
<head>
<meta charset="utf-8">
<title>Korvan Shield Group – Business Card</title>
<link href="https://fonts.googleapis.com/css2?family=Barlow+Condensed:wght@300;400;600&display=swap" rel="stylesheet">
<style>
  :root {
    --backdrop: #e4e4e2;
    --brand-blue: #0a6fb7;
    --ink-grey: #5f5f5f;
    --paper: #ffffff;
    --card-shadow: 6px 8px 14px rgba(0,0,0,0.18);
  }
  * { margin: 0; padding: 0; box-sizing: border-box; }
  html, body { width: 1200px; height: 846px; overflow: hidden; background: var(--backdrop); }
  body { position: relative; font-family: "Barlow Condensed", "Arial Narrow", sans-serif; }

  .card {
    position: absolute; left: 347px; width: 509px; height: 291px;
    box-shadow: var(--card-shadow);
  }
  .card--front { top: 99px; background: var(--paper); }
  .card--back { top: 457px; background: var(--brand-blue); }

  /* Wordmark */
  .wordmark {
    position: absolute; display: flex; align-items: center; gap: 10px;
    font-weight: 600; text-transform: uppercase; line-height: 0.95; letter-spacing: 1px;
  }
  .wordmark__square { width: 38px; height: 38px; flex: none; }
  .wordmark__name { font-size: 34px; }
  .card--front .wordmark { left: 26px; top: 128px; width: 250px; color: var(--brand-blue); }
  .card--front .wordmark__square { background: var(--brand-blue); }
  .card--back .wordmark { left: 0; right: 0; top: 58px; justify-content: center; color: var(--paper); }
  .card--back .wordmark__square { background: var(--paper); }

  /* Contact block */
  .contact-divider {
    position: absolute; left: 285px; top: 133px; width: 1px; height: 95px; background: var(--ink-grey);
  }
  .contact {
    position: absolute; left: 295px; top: 128px; color: var(--ink-grey);
    font-weight: 300; font-size: 16px; line-height: 18px; white-space: nowrap;
  }
  .contact__name { font-size: 17px; margin-bottom: 9px; }
  .contact__name strong, .contact__label { color: var(--brand-blue); font-weight: 600; }

  /* Services row */
  .services {
    position: absolute; left: 18px; right: 18px; top: 176px;
    display: flex; justify-content: space-between; list-style: none;
  }
  .service {
    width: 81px; display: flex; flex-direction: column; align-items: center;
    color: var(--paper); font-size: 12px; line-height: 14px; text-align: center; text-transform: uppercase;
  }
  .service svg { width: 46px; height: 36px; margin-bottom: 9px; fill: var(--paper); }
</style>
</head>
<body>

<section class="card card--front">
  <div class="wordmark">
    <span class="wordmark__square"></span>
    <span class="wordmark__name">Korvan Shield<br>Group</span>
  </div>
  <div class="contact-divider"></div>
  <div class="contact">
    <p class="contact__name"><strong>Brent Holloway</strong> Owner</p>
    <p><span class="contact__label">Office:</span> 780.555.0148</p>
    <p><span class="contact__label">Cell:</span> 780.555.0193</p>
    <p>brent@korvanshieldgroup.example</p>
    <p>20417 163 St Edmonton, AB T5X 2K8</p>
  </div>
</section>

<section class="card card--back">
  <div class="wordmark">
    <span class="wordmark__square"></span>
    <span class="wordmark__name">Korvan Shield Group</span>
  </div>

  <ul class="services">
    <li class="service">
      <svg viewBox="0 0 46 36" aria-hidden="true"><path d="M15 0h16v34h2v2H13v-2h2zM18 4v3h3V4zm6 0v3h3V4zM18 10v3h3v-3zm6 0v3h3v-3zM18 16v3h3v-3zm6 0v3h3v-3zM21 28v6h4v-6z" fill-rule="evenodd"/></svg>
      Exterior &amp;<br>Interior Patrols
    </li>
    <li class="service">
      <svg viewBox="0 0 46 36" aria-hidden="true"><path d="M13 2h20l5 9h4v4h-3v15h-6v-4H13v4H7V15H4v-4h4zm2 3-3 6h22l-3-6zM11 17a3 3 0 1 0 6 0 3 3 0 1 0-6 0zm18 0a3 3 0 1 0 6 0 3 3 0 1 0-6 0z" fill-rule="evenodd"/></svg>
      Incident<br>Response
    </li>
    <li class="service">
      <svg viewBox="0 0 46 36" aria-hidden="true"><circle cx="14" cy="9" r="8"/><path d="M0 35c0-9 6-14 14-14s14 5 14 14z"/><circle cx="34" cy="12" r="7"/><path d="M29 35c0-5-1-9-4-12 3-2 6-3 9-3 7 0 12 4 12 12v3z"/></svg>
      Safety<br>Escorts
    </li>
    <li class="service">
      <svg viewBox="0 0 46 36" aria-hidden="true"><circle cx="17" cy="9" r="8"/><path d="M3 35c0-9 6-14 14-14 4 0 7 1 9 3v11z"/><path d="M36 17l9 3c0 8-3 13-9 16-6-3-9-8-9-16zm0 3v13c4-2 6-6 6-11z" fill-rule="evenodd"/></svg>
      Alarm<br>Response
    </li>
    <li class="service">
      <svg viewBox="0 0 46 36" aria-hidden="true"><circle cx="16" cy="9" r="8"/><path d="M2 35c0-9 6-14 14-14 3 0 6 1 8 2v12z"/><path d="M30 18v-3a6 6 0 0 1 12 0v3h2v17H28V18zm3 0h6v-3a3 3 0 0 0-6 0zm3 7a2 2 0 1 0 0 4 2 2 0 1 0 0-4z" fill-rule="evenodd"/></svg>
      Lock &amp;<br>Unlock
    </li>
    <li class="service">
      <svg viewBox="0 0 46 36" aria-hidden="true"><path d="M18 1l18 14h-5v2H21v17H6V15H0zm8 2h4v6l-4-3z"/><path d="M21 19h20v13h4v3H19v-3h2zm3 3v10h14V22z" fill-rule="evenodd"/></svg>
      Online<br>Reporting
    </li>
  </ul>
</section>

</body>
</html>
```